HollowPine Ventures Inc. Business Card Design

My business is custom renovations and homes.I would need to have a new business logo created to go along with my company name. The business card should be of a modern style as this is the market I am focused on. I would need my contact information and website posted on the card. I would also like to list a few of the tasks I conduct on the card (such as: Renovations, Additions, Repairs, New Homes, Design, Consultations). On the reverse of the card I currently have just my logo and my motto, "Shaping A Bold Path". However, I am open to completely changing everything as I am starting a new year and would like to excel further. Any new ideas and suggestions are always welcomed. Thank you.

Target Market(s)

Upscale residential and commercial renovations and builds

Industry/Entity Type

Business

Contact Information for Business Card

I would like the design to be able to be laser cut or burnt onto a wooden business card. I will be creating one option of cards for really loyal customers (wooden) and a second option for the everyday customer (paper).

Font styles to use
Other font styles liked:
• Calibri / anything of mordern taste

Colors
f37122
5c5c5c
474747
ffffff

Requirements
Must have
• I would like the colours of my business to be a sharp orange and grey. I believe this will symbolize a modern style. I am open to other suggestions if this is not suitable for the designers tastes. My contact info as follows:
• Will Marsh
• President
• HollowPine Ventures Inc.
• 555-214-3987
• will@hollowpineventures.example
• I would like my website (currently under construction) hollowpineventures.example on the card aswell.
Nice to have
• Along with a modern logo representing HollowPine, I would like something on the card besides the logo and contact information. Perhaps a small background design. I feel it may be nice to have my services listed on the card (in smaller font on the bottom) Renovations, Additions, Repairs, Design, Consultations.
Should not have
• The business card should not have too many different colors. Should not have rounded corners.

```html
<!DOCTYPE html>
<html lang="en">
<head>
<meta charset="utf-8">
<title>HollowPine Ventures Inc. – Business Card</title>
<link href="https://fonts.googleapis.com/css2?family=Open+Sans:wght@400;600;700&display=swap" rel="stylesheet">
<style>
  :root {
    --orange: #f37122;
    --grey: #5c5c5c;
    --grey-dark: #474747;
    --paper: #ffffff;
    --backdrop: #d9d9d9;
  }
  html, body {
    margin: 0;
    padding: 0;
    width: 1200px;
    height: 864px;
    overflow: hidden;
    background: var(--backdrop);
    font-family: "Open Sans", Arial, sans-serif;
  }
  .canvas {
    position: relative;
    width: 1200px;
    height: 864px;
  }
  .card {
    position: absolute;
    width: 560px;
    height: 320px;
    background: var(--paper);
    box-shadow: 0 6px 18px rgba(0,0,0,0.18);
  }
  .card--back { left: 580px; top: 70px; }
  .card--front { left: 60px; top: 480px; }

  .brand {
    position: absolute;
    left: 0;
    right: 0;
    display: flex;
    align-items: center;
    justify-content: center;
    gap: 12px;
  }
  .brand__square {
    width: 22px;
    height: 22px;
    background: var(--orange);
  }
  .brand__name {
    font-weight: 700;
    color: var(--grey-dark);
    letter-spacing: 0.5px;
  }
  .card--back .brand { top: 110px; }
  .card--back .brand__name { font-size: 30px; }
  .card--front .brand { top: 58px; }
  .card--front .brand__name { font-size: 26px; }

  .services {
    position: absolute;
    left: 0;
    right: 0;
    bottom: 46px;
    text-align: center;
    font-size: 14px;
    font-weight: 600;
    color: var(--grey-dark);
    letter-spacing: 1px;
  }
  .services .sep { margin: 0 6px; }

  .person {
    position: absolute;
    left: 40px;
    top: 170px;
    width: 200px;
    text-align: right;
  }
  .person__name {
    font-size: 26px;
    font-weight: 700;
    color: var(--grey);
    line-height: 1.1;
  }
  .person__title {
    font-size: 18px;
    color: var(--orange);
  }
  .divider {
    position: absolute;
    left: 262px;
    top: 160px;
    width: 2px;
    height: 110px;
    background: var(--grey);
  }
  .contact {
    position: absolute;
    left: 284px;
    top: 168px;
    list-style: none;
    margin: 0;
    padding: 0;
  }
  .contact__item {
    display: flex;
    align-items: center;
    gap: 10px;
    font-size: 15px;
    color: var(--grey-dark);
    height: 30px;
  }
  .contact__icon {
    width: 18px;
    height: 18px;
    flex: none;
  }
</style>
</head>
<body>
<main class="canvas">

  <section class="card card--back" aria-label="Card reverse">
    <div class="brand">
      <span class="brand__square"></span>
      <span class="brand__name">HollowPine Ventures Inc.</span>
    </div>
    <p class="services">Renovations<span class="sep">|</span>Additions<span class="sep">|</span>Repairs<span class="sep">|</span>New Homes<span class="sep">|</span>Consultations</p>
  </section>

  <section class="card card--front" aria-label="Card front">
    <div class="brand">
      <span class="brand__square"></span>
      <span class="brand__name">HollowPine Ventures Inc.</span>
    </div>

    <div class="person">
      <div class="person__name">Will Marsh</div>
      <div class="person__title">President</div>
    </div>

    <div class="divider"></div>

    <ul class="contact">
      <li class="contact__item">
        <svg class="contact__icon" viewBox="0 0 18 18" aria-hidden="true">
          <rect width="18" height="18" fill="var(--orange)"/>
          <path d="M5.5 4 L7.5 4 L8.3 6.8 L7 7.8 C7.6 9.3 8.7 10.4 10.2 11 L11.2 9.7 L14 10.5 L14 12.5 C14 13.3 13.3 14 12.5 14 C8.4 13.7 4.3 9.6 4 5.5 C4 4.7 4.7 4 5.5 4 Z" fill="#fff"/>
        </svg>
        <span>555-214-3987</span>
      </li>
      <li class="contact__item">
        <svg class="contact__icon" viewBox="0 0 18 18" aria-hidden="true">
          <rect width="18" height="18" fill="var(--orange)"/>
          <rect x="3.5" y="5" width="11" height="8" fill="none" stroke="#fff" stroke-width="1.3"/>
          <path d="M3.5 5 L9 9.5 L14.5 5" fill="none" stroke="#fff" stroke-width="1.3"/>
        </svg>
        <span>will@hollowpineventures.example</span>
      </li>
      <li class="contact__item">
        <svg class="contact__icon" viewBox="0 0 18 18" aria-hidden="true">
          <rect width="18" height="18" fill="var(--orange)"/>
          <circle cx="9" cy="9" r="5.2" fill="none" stroke="#fff" stroke-width="1.3"/>
          <ellipse cx="9" cy="9" rx="2.2" ry="5.2" fill="none" stroke="#fff" stroke-width="1.1"/>
          <line x1="3.8" y1="9" x2="14.2" y2="9" stroke="#fff" stroke-width="1.1"/>
        </svg>
        <span>www.hollowpineventures.example</span>
      </li>
    </ul>
  </section>

</main>
</body>
</html>
```